Building Company Business Card Design

I am looking to get a business card designed for my Building Company. Please find the logo attached.

Industry/Entity Type

Business

Contact Information for Business Card

Mobile 0472 913 046
Email admin@tarrowconstructworks.com.au
Website www.tarrowconstructworks.com.au

Colors
0255a3

```html
<!DOCTYPE html>
<html lang="en">
<head>
<meta charset="utf-8">
<title>Tarrow Construct Works — Business Card</title>
<link href="https://fonts.googleapis.com/css2?family=Montserrat:wght@400;600;700&display=swap" rel="stylesheet">
<style>
  :root {
    --brand-blue: #0255a3;
    --ink-grey: #58585c;
    --wave-grey: #5a5960;
    --card-white: #ffffff;
    --page-bg: #e6e7ea;
  }
  * { box-sizing: border-box; margin: 0; padding: 0; }
  html, body { width: 1200px; height: 810px; overflow: hidden; }
  body {
    background: var(--page-bg);
    font-family: "Montserrat", Arial, sans-serif;
    display: flex;
    flex-direction: column;
    align-items: center;
    justify-content: center;
    gap: 44px;
  }
  .card {
    position: relative;
    width: 560px;
    height: 320px;
    overflow: hidden;
    box-shadow: 0 6px 18px rgba(0,0,0,0.18);
  }

  /* Front */
  .card-front {
    background: var(--brand-blue);
    color: var(--card-white);
    display: flex;
    flex-direction: column;
    align-items: center;
    justify-content: center;
  }
  .brand-name {
    font-weight: 700;
    text-transform: uppercase;
    letter-spacing: 1px;
    line-height: 1.05;
    text-align: center;
  }
  .card-front .brand-name { font-size: 34px; color: var(--card-white); }
  .front-url {
    position: absolute;
    bottom: 44px;
    left: 0; right: 0;
    text-align: center;
    font-size: 13px;
    letter-spacing: 0.5px;
  }

  /* Back */
  .card-back { background: var(--card-white); }
  .back-wave { position: absolute; inset: 0; }
  .back-content {
    position: absolute;
    top: 66px;
    left: 30px;
    right: 16px;
    display: flex;
    align-items: center;
  }
  .card-back .brand-name {
    font-size: 21px;
    color: var(--brand-blue);
    width: 190px;
    text-align: left;
  }
  .divider {
    width: 2px;
    height: 108px;
    background: var(--brand-blue);
    margin: 0 20px 0 12px;
    flex: none;
  }
  .person-name {
    font-size: 17px;
    font-weight: 600;
    color: var(--brand-blue);
    letter-spacing: 0.5px;
    text-transform: uppercase;
  }
  .person-role {
    font-size: 11px;
    color: var(--ink-grey);
    margin: 2px 0 10px;
  }
  .contact-list { list-style: none; }
  .contact-list li {
    display: flex;
    align-items: center;
    gap: 9px;
    font-size: 12px;
    color: var(--ink-grey);
    margin-bottom: 4px;
    white-space: nowrap;
  }
  .contact-icon { width: 11px; height: 11px; fill: var(--brand-blue); flex: none; }
</style>
</head>
<body>

  <section class="card card-front">
    <div class="brand-name">Tarrow<br>Construct Works</div>
    <div class="front-url">www.tarrowconstructworks.com.au</div>
  </section>

  <section class="card card-back">
    <svg class="back-wave" viewBox="0 0 560 320" preserveAspectRatio="none" aria-hidden="true">
      <path d="M0,300 C170,245 360,250 560,196" fill="none" stroke="var(--wave-grey)" stroke-width="5"/>
      <path d="M0,314 C175,260 365,265 560,210 L560,320 L0,320 Z" fill="var(--brand-blue)"/>
    </svg>

    <div class="back-content">
      <div class="brand-name">Tarrow<br>Construct Works</div>
      <div class="divider"></div>
      <div class="person">
        <div class="person-name">Daniel Harper</div>
        <div class="person-role">Director</div>
        <ul class="contact-list">
          <li>
            <svg class="contact-icon" viewBox="0 0 24 24"><path d="M6.6 10.8a15.1 15.1 0 0 0 6.6 6.6l2.2-2.2a1 1 0 0 1 1-.25 11.4 11.4 0 0 0 3.6.57 1 1 0 0 1 1 1V20a1 1 0 0 1-1 1A17 17 0 0 1 3 4a1 1 0 0 1 1-1h3.5a1 1 0 0 1 1 1c0 1.25.2 2.45.57 3.57a1 1 0 0 1-.25 1z"/></svg>
            0472 913 046
          </li>
          <li>
            <svg class="contact-icon" viewBox="0 0 24 24"><path d="M2 5h20v14H2z M2 5l10 8 10-8" /></svg>
            admin@tarrowconstructworks.com.au
          </li>
          <li>
            <svg class="contact-icon" viewBox="0 0 24 24"><circle cx="12" cy="12" r="10"/></svg>
            www.tarrowconstructworks.com.au
          </li>
        </ul>
      </div>
    </div>
  </section>

</body>
</html>
```